Advertisement Design Project

Attached is the information I need in a big color ad

10X11 that will go in a weekly local paper.
I am open to color and graphics-no pictures of people please.

My logo is also attached, which I would like in the ad.

Sorry for the short notice-I just got a deal on the space and it is due Friday.

```html
<!DOCTYPE html>
<html lang="en">
<head>
<meta charset="utf-8">
<title>New Tax Laws – Estate Planning Workshop</title>
<link href="https://fonts.googleapis.com/css2?family=Noto+Sans:ital,wght@0,400;0,700;0,800;1,700;1,800&family=Roboto+Condensed:wght@400;700&display=swap" rel="stylesheet">
<style>
  :root {
    --page: #ffffff;
    --panel: #0a6cb5;
    --panel-deep: #0b4a86;
    --white: #ffffff;
    --gold: #f7c300;
    --cream: #fdf6a3;
    --navy: #0c2140;
    --faint: #1b61a3;
  }
  * { margin: 0; padding: 0; box-sizing: border-box; }
  html, body { width: 1200px; height: 1000px; overflow: hidden; background: var(--page); }
  .canvas { position: relative; width: 1200px; height: 1000px; font-family: "Noto Sans", Verdana, sans-serif; }
  .ad-panel { position: absolute; left: 188px; top: 46px; width: 824px; height: 906px; background: var(--panel); overflow: hidden; }
  .ad-panel svg.shade { position: absolute; left: 0; top: 0; }
  .abs { position: absolute; white-space: nowrap; transform-origin: left top; }

  .headline { left: 50px; top: 18px; font-size: 82px; font-weight: 800; font-style: italic; color: var(--white); transform: scaleX(1.17); }
  .subhead { left: 94px; top: 114px; font-size: 72px; font-weight: 800; font-style: italic; color: var(--gold); transform: scaleX(1.2); }
  .topics { left: 90px; top: 192px; font-size: 35px; font-weight: 700; color: var(--cream); transform: scaleX(1.1); }

  .questions { left: 0; top: 298px; list-style: none; font-size: 16px; color: var(--white); line-height: 22.4px; }
  .questions li { white-space: nowrap; }

  .faint-mark { left: 578px; top: 400px; font-size: 26px; font-weight: 800; color: var(--faint); }

  .cta { left: 249px; top: 638px; font-size: 28px; font-weight: 800; font-style: italic; line-height: 30px; color: var(--white); transform: scaleX(1.15); }
  .cta span { display: block; color: var(--gold); }

  .brand { left: 32px; top: 808px; font-size: 20px; font-weight: 700; color: var(--cream); display: flex; align-items: center; gap: 8px; }
  .brand i { width: 14px; height: 14px; border-radius: 50%; background: var(--gold); display: inline-block; }

  .details { font-family: "Roboto Condensed", "Arial Narrow", sans-serif; font-weight: 700; }
  .presented { left: 281px; top: 728px; font-size: 17px; color: var(--white); }
  .presenter { left: 281px; top: 750px; font-size: 20px; color: var(--navy); }
  .presenter small { font-size: 12px; margin-left: 4px; }
  .office { left: 283px; top: 774px; font-size: 13px; color: var(--white); }
  .timing { left: 272px; top: 797px; width: 226px; height: 42px; border: 1px solid var(--white); padding: 5px 8px; font-size: 10.5px; line-height: 14px; color: var(--white); }
  .venue { left: 281px; top: 846px; font-size: 11px; line-height: 14px; color: var(--white); }

  .tagline { left: 564px; top: 749px; font-size: 20px; color: var(--white); }
  .tagline-sub { left: 564px; top: 775px; font-size: 11px; color: var(--navy); }
  .phone { left: 564px; top: 818px; font-size: 11px; color: var(--white); }
  .slogan { left: 564px; top: 866px; font-family: "Noto Sans", Verdana, sans-serif; font-size: 18px; font-weight: 800; font-style: italic; color: var(--white); transform: scaleX(1.16); }
  .slogan span { color: var(--cream); }
</style>
</head>
<body>
<div class="canvas">
  <section class="ad-panel">
    <svg class="shade" width="824" height="906" viewBox="0 0 824 906" aria-hidden="true">
      <defs>
        <linearGradient id="shadeGrad" x1="0" y1="0" x2="0" y2="1">
          <stop offset="0" stop-color="#0a6cb5" stop-opacity="0"/>
          <stop offset="0.35" stop-color="#0a66ad"/>
          <stop offset="1" stop-color="#0b4a86"/>
        </linearGradient>
      </defs>
      <path d="M0,0 L120,0 C150,320 200,620 248,906 L0,906 Z" fill="url(#shadeGrad)"/>
    </svg>

    <h1 class="abs headline">New Tax Laws</h1>
    <h2 class="abs subhead">Trusts</h2>
    <h3 class="abs topics">Annuities and Long Term Care</h3>

    <ul class="abs questions">
      <li style="padding-left:142px">Is a living trust right for me?</li>
      <li style="padding-left:146px">Does my existing Trust need to be changed?</li>
      <li style="padding-left:155px">Why does Joint Tenancy create tax problems?</li>
      <li style="padding-left:166px">I have a Will, isn’t that enough?</li>
      <li style="padding-left:175px">Why do I need powers of attorney?</li>
      <li style="padding-left:184px">How much are inheritance taxes?</li>
      <li style="padding-left:192px">What are the new Affordable Care Act Taxes?</li>
      <li style="padding-left:200px">How does Long Term Care insurance work?</li>
      <li style="padding-left:207px">The average cost of long term care is over</li>
      <li style="padding-left:213px">80K a year-</li>
      <li style="padding-left:220px">how do I plan for those costs?</li>
      <li style="padding-left:225px">The truth about annuities-</li>
      <li style="padding-left:230px">What are the biggest mistakes in estate</li>
      <li style="padding-left:235px">planning?</li>
    </ul>

    <div class="abs faint-mark">Harbor Lane Law</div>

    <p class="abs cta">Come learn <span>what you need to know</span></p>

    <div class="abs brand"><i></i>Harbor Lane Law</div>

    <p class="abs details presented">Presented by:</p>
    <p class="abs details presenter">marla jean whitcomb <small>Attorney at Law</small></p>
    <p class="abs details office">2140 Alder Street, Brookvale.</p>
    <div class="abs details timing">WORKSHOP TIMING<br>September 19, 2013, 1-2:30pm,&nbsp;&nbsp; 6-7:30pm</div>
    <p class="abs details venue">Coastline Inn, Rivermont<br>4820 Meadow Crest Court<br>Rivermont, California 90000</p>

    <p class="abs details tagline">Helping&nbsp; Families</p>
    <p class="abs details tagline-sub">plan their estates for over 20 years.</p>
    <p class="abs details phone">please call:(555) 014 - 2290</p>
    <p class="abs slogan">Be Smart. <span>Plan Ahead.</span></p>
  </section>
</div>
</body>
</html>
```